Offshore Energy Projects Management Consultancy needs a business card design

Logo available. We provide teams to deliver engineering consultancy, project management and delivery teams mainly in the offshore renewables sector. The company is all about bringing the right people to a project to deliver the scope.

The business card will be used for all staff.

The business card should be quite simple, vibrant and uncluttered but convey experience, enthusiasm and integration.

Target Market(s)

Energy Project Developers and Tier 1 construction companies

Contact Information for Business Card

Logo should be on the back of the card. I'm happy for the designer to play with the colour of the logo and background colour.

Front of the card should convey all the must have information in a clear and professional manner but without being overly traditional.

Colors

Designer to choose colors to be used in the design.

Requirements
Must have
• Land Line Tel Number, Mobile Tel Number, Email, business address, web address.

```html
<!DOCTYPE html>
<html lang="en">
<head>
<meta charset="utf-8">
<title>Tidewater Delivery Partners – Business Card</title>
<link href="https://fonts.googleapis.com/css2?family=Exo+2:wght@400;500;600&display=swap" rel="stylesheet">
<style>
  :root {
    --stage: #4d4e4e;
    --paper: #ffffff;
    --brand-blue: #1474bf;
    --brand-sky: #25a9e0;
    --brand-grey: #6d6e71;
    --ink: #555659;
  }
  * { box-sizing: border-box; margin: 0; padding: 0; }
  html, body {
    width: 963px; height: 1200px; overflow: hidden;
    background: var(--stage);
    font-family: "Exo 2", sans-serif;
  }
  .card {
    position: absolute;
    left: 231px;
    width: 560px;
    height: 320px;
  }
  .card--front { top: 221px; background: var(--paper); }
  .card--back { top: 634px; background: var(--brand-sky); }

  .front-wordmark {
    position: absolute;
    left: 40px; top: 120px;
    width: 240px;
    display: flex; align-items: center; justify-content: center; gap: 10px;
    color: var(--brand-grey);
    font-weight: 600; font-size: 17px; line-height: 1.15;
    text-transform: uppercase; letter-spacing: 0.2px;
  }
  .front-wordmark .mark-square {
    width: 30px; height: 30px; background: var(--brand-blue); flex: none;
  }
  .divider {
    position: absolute;
    left: 301px; top: 83px;
    width: 1.5px; height: 152px;
    background: var(--brand-grey);
  }
  .contact {
    position: absolute;
    left: 323px; top: 80px;
    color: var(--ink);
    font-size: 13px; line-height: 16px;
  }
  .contact .name {
    color: var(--brand-blue);
    font-size: 19px; font-weight: 600; line-height: 22px;
  }
  .contact .role { font-size: 12.5px; font-weight: 500; margin-bottom: 8px; }
  .contact .address { margin-bottom: 8px; }
  .contact .web { color: var(--brand-blue); }

  .bands {
    position: absolute; left: 0; right: 0; bottom: 0;
    height: 9px; display: flex; gap: 2px;
  }
  .bands span { flex: 1; }
  .bands .band-blue { background: var(--brand-blue); }
  .bands .band-grey { background: var(--brand-grey); }
  .bands .band-sky { background: var(--brand-sky); }

  .back-wordmark {
    position: absolute; left: 0; right: 0; top: 128px;
    display: flex; align-items: center; justify-content: center; gap: 14px;
    color: var(--paper);
    font-weight: 600; font-size: 24px;
    text-transform: uppercase; letter-spacing: 0.3px;
  }
  .back-wordmark .mark-square {
    width: 38px; height: 38px; background: var(--paper);
  }
</style>
</head>
<body>
  <section class="card card--front" aria-label="Card front">
    <div class="front-wordmark">
      <span class="mark-square"></span>
      <span>Tidewater<br>Delivery Partners</span>
    </div>
    <div class="divider"></div>
    <div class="contact">
      <p class="name">Daniel Hale</p>
      <p class="role">President</p>
      <p class="address">412 Harbor View Road<br>Seward, Alaska 34610</p>
      <p>P. 555-204-7731</p>
      <p>M. 555-318-6042</p>
      <p>hello@tidewaterpartners.com</p>
      <p class="web">www.tidewaterpartners.com</p>
    </div>
    <div class="bands">
      <span class="band-blue"></span>
      <span class="band-grey"></span>
      <span class="band-sky"></span>
    </div>
  </section>

  <section class="card card--back" aria-label="Card back">
    <div class="back-wordmark">
      <span class="mark-square"></span>
      <span>Tidewater Delivery Partners</span>
    </div>
  </section>
</body>
</html>
```